Business Card Design Project

for a second hand vintage clothing store. shop name is The Velvet Cupboard

Cards to be double sided

The name on the card is Joanna Whitfield

Information to put on card:

The Velvet Cupboard
Joanna Whitfield (no job title)
42/871 Dunmore St, Glenwick, Sydney, NSW, 2009.
Mobile: 0412 905 261
Email: thevelvetcupboard@mailbox.com.au
Web: www.thevelvetcupboard.com.au

Target Market(s)

Women looking at vintage clothing

Industry/Entity Type

Clothing

```html
<!DOCTYPE html>
<html lang="en">
<head>
<meta charset="utf-8">
<title>The Velvet Cupboard – Business Card</title>
<link rel="stylesheet" href="https://fonts.googleapis.com/css2?family=Rochester&display=block">
<style>
  :root {
    --card-gold: #b38e2e;
    --brand-plum: #5e2a3f;
    --brand-cream: #efe0a9;
    --ink: #1f1b17;
    --edge: #7a7a7a;
  }
  * { margin: 0; padding: 0; box-sizing: border-box; }
  html, body {
    width: 1200px;
    height: 676px;
    overflow: hidden;
    background: var(--card-gold);
  }
  .card {
    position: relative;
    width: 1200px;
    height: 676px;
    background: var(--card-gold);
    border: 1px solid var(--edge);
    font-family: "Rochester", "Brush Script MT", "Segoe Script", cursive;
    color: var(--ink);
  }
  .brand-panel {
    position: absolute;
    left: 34px;
    top: 21px;
    width: 572px;
    height: 267px;
    background: var(--brand-plum);
    display: flex;
    align-items: center;
    justify-content: center;
  }
  .brand-name {
    font-size: 66px;
    line-height: 1;
    color: var(--brand-cream);
    font-weight: 400;
    white-space: nowrap;
  }
  .person-name {
    position: absolute;
    left: 331px;
    top: 470px;
    font-size: 110px;
    line-height: 1;
    font-weight: 400;
    letter-spacing: 3px;
    white-space: nowrap;
  }
  .mobile {
    position: absolute;
    left: 333px;
    top: 603px;
    font-size: 42px;
    line-height: 1;
    font-weight: 400;
    letter-spacing: 1px;
    white-space: nowrap;
  }
</style>
</head>
<body>
  <div class="card">
    <div class="brand-panel">
      <span class="brand-name">The Velvet Cupboard</span>
    </div>
    <p class="person-name">Joanna Whitfield</p>
    <p class="mobile">Mobile: 0412 905 261</p>
  </div>
</body>
</html>
```